I need a book cover design for my book "Roaming Quartets." It is a non-fiction book focused on answering the question of whether American evangelicals look more like the Quartets than Jesus.

The subtitle is "The Curious Habits of Norway's Traveling Fiddlers and Their Seaside Rivals." The author name is Dorian Whitlock.

I will be publishing this as an ebook and paperback.

I am open to all ideas, but will share the only thought I had as a possible design. In the title, the third letter in both words is "A." I thought about the idea of having the "A" in "Roaming" have a halo and the "A" in "Quartets" somehow seem to be a shadow of that first "A" but have devil horns instead of a halo. Again, I'm not sold on that, but am sharing it as one design possibility.

I am not interested in the book cover design having a cheesy religious look to it (as many do). I am more interested in it looking like a professional non-fiction cover.

```html
<!DOCTYPE html>
<html lang="en">
<head>
<meta charset="UTF-8">
<title>Roaming Quartets — Book Cover</title>
<link rel="stylesheet" href="https://fonts.googleapis.com/css2?family=Archivo+Black&family=Open+Sans:wght@400&display=swap">
<style>
  :root {
    --stage-bg: #e9edf1;
    --cover-bg: #fbfbfb;
    --cover-shade: #ececec;
    --art-tone-a: rgba(200, 200, 200, 0.35);
    --art-tone-b: rgba(230, 230, 230, 0.15);
    --subtitle-ink: #3c3c3c;
    --title-blue-dark: #174a86;
    --title-blue-mid: #1f6fae;
    --title-teal: #2aa3c9;
    --title-orange-dark: #e0602a;
    --title-orange-light: #f2a04a;
    --author-ink: #1a1a1a;
  }
  * { margin: 0; padding: 0; box-sizing: border-box; }
  html, body {
    width: 1200px;
    height: 960px;
    overflow: hidden;
    background: var(--stage-bg);
  }
  .canvas {
    position: relative;
    width: 1200px;
    height: 960px;
  }
  .book-cover {
    position: absolute;
    left: 308px;
    top: 30px;
    width: 585px;
    height: 900px;
    background: linear-gradient(135deg, var(--cover-bg) 0%, #f4f4f4 60%, var(--cover-shade) 100%);
    overflow: hidden;
    box-shadow: 0 6px 24px rgba(0, 0, 0, 0.12);
  }
  .background-artwork {
    position: absolute;
    inset: 0;
    background:
      radial-gradient(ellipse 40% 30% at 18% 22%, var(--art-tone-a), transparent 70%),
      radial-gradient(ellipse 55% 60% at 70% 55%, var(--art-tone-b), transparent 75%),
      linear-gradient(160deg, transparent 30%, var(--art-tone-b) 60%, transparent 85%);
  }
  .subtitle {
    position: absolute;
    top: 96px;
    left: 0;
    right: 0;
    text-align: center;
    font-family: "Open Sans", sans-serif;
    font-size: 15.5px;
    line-height: 1.65;
    letter-spacing: 0.2px;
    text-transform: uppercase;
    color: var(--subtitle-ink);
  }
  .title-block {
    position: absolute;
    left: 50%;
    top: 48%;
    transform: translate(-50%, -50%) rotate(-42deg);
    white-space: nowrap;
  }
  .title-word {
    display: block;
    font-family: "Archivo Black", sans-serif;
    font-size: 64px;
    line-height: 0.95;
    text-transform: uppercase;
    -webkit-background-clip: text;
    background-clip: text;
    color: transparent;
  }
  .title-word--first {
    background-image: linear-gradient(90deg, var(--title-blue-dark) 0%, var(--title-blue-mid) 50%, var(--title-teal) 100%);
  }
  .title-word--second {
    margin-left: 92px;
    background-image: linear-gradient(90deg, var(--title-orange-dark) 0%, var(--title-orange-light) 100%);
  }
  .author-name {
    display: block;
    margin-left: 150px;
    margin-top: 4px;
    font-family: "Archivo Black", sans-serif;
    font-size: 18px;
    letter-spacing: 0.5px;
    text-transform: uppercase;
    color: var(--author-ink);
  }
</style>
</head>
<body>
  <main class="canvas">
    <section class="book-cover">
      <div class="background-artwork" role="img" aria-label="Faint still life of an ink bottle, a fountain pen and a handwritten letter on white paper"></div>
      <p class="subtitle">The Curious Habits of Norway's Traveling Fiddlers<br>and Their Seaside Rivals</p>
      <h1 class="title-block">
        <span class="title-word title-word--first">Roaming</span>
        <span class="title-word title-word--second">Quartets</span>
        <span class="author-name">Dorian Whitlock</span>
      </h1>
    </section>
  </main>
</body>
</html>
```